Stationary Design to Complement our Website

We would like template designed for word documents that we can use for headed paper. The template should complement the style of our website & incorporate our existing logo. https://www.velmorantravel.com/

The header and footer design should be sperate PNG or JPEG files that we can copy and paste into word header and footers. They should work on A4 & letter sized papers.

Note the main web colours are as follows:

Black
HEX code #2b2c2b
C=71 M=64 Y=64 K=65
RGB 43,44,43

Green
HEX code #116c49
C=88 M=33 Y=82 K=24
RGB 17,108,73

Current fonts are ALEO & Gilroy.

Fonts and colours in new design don't have to match website exactly but should be complementary.

Font styles to use
Serif

Requirements
Must have
• a simple design that complements our website.
Some kind of graphic on the top & some sort of graphic on the bottom. Not just plain logo on top.
designs that incorporate the clouds might look good
Can also incorporate 5* rate harbor rating
Should not have
• no photographs included on the design

```html
<!DOCTYPE html>
<html lang="en">
<head>
<meta charset="utf-8">
<title>Velmoran Travel – Letterhead</title>
<link rel="stylesheet" href="https://fonts.googleapis.com/css2?family=Aleo:wght@400;500&family=Lato:wght@400;700&display=swap">
<style>
  :root {
    --backdrop: #48494d;
    --paper: #ffffff;
    --brand-green: #116c49;
    --leaf-green: #86a93a;
    --ink: #2b2c2b;
    --body-grey: #5a5a5a;
    --signature-tone: #c9d3e2;
  }
  * { margin: 0; padding: 0; box-sizing: border-box; }
  html, body { width: 1200px; height: 900px; overflow: hidden; background: var(--backdrop); }
  .letterhead {
    position: absolute; left: 296px; top: 20px;
    width: 609px; height: 861px;
    background: var(--paper);
    font-family: "Lato", Arial, sans-serif;
    color: var(--ink);
  }
  .top-band { position: absolute; left: 0; top: 0; width: 100%; height: 10px; background: var(--leaf-green); }
  .brand { position: absolute; left: 43px; top: 46px; display: flex; align-items: flex-start; gap: 9px; }
  .brand-dot { width: 14px; height: 14px; border-radius: 50%; background: var(--brand-green); margin-top: 4px; }
  .brand-name {
    font-family: "Aleo", Georgia, serif; font-weight: 400;
    font-size: 30px; line-height: 40px; letter-spacing: 5px; color: var(--ink);
  }
  .address {
    position: absolute; left: 387px; top: 56px;
    border-left: 1.5px solid var(--leaf-green); padding-left: 7px;
    font-family: "Aleo", Georgia, serif; font-size: 10px; line-height: 17px; color: var(--ink);
  }
  .letter { position: absolute; left: 53px; top: 222px; width: 512px; }
  .letter-date { font-size: 10px; font-weight: 700; color: var(--ink); }
  .letter-topic { font-size: 10px; font-weight: 700; margin-top: 26px; }
  .letter-body p {
    font-size: 9.4px; line-height: 12.3px; color: var(--body-grey);
    text-align: justify; margin-top: 12px;
  }
  .letter-body p:first-child { margin-top: 22px; }
  .signature {
    position: absolute; left: 53px; top: 624px; width: 152px; height: 44px;
    background: linear-gradient(90deg, var(--signature-tone), #eef1f6);
    border-radius: 4px;
  }
  .contacts { position: absolute; left: 0; top: 752px; width: 100%; }
  .contact { position: absolute; width: 150px; margin-left: -75px; text-align: center; }
  .contact svg { display: block; margin: 0 auto; }
  .contact-number { font-size: 10px; font-weight: 700; margin-top: 9px; letter-spacing: -0.2px; }
  .contact-label { font-family: "Aleo", Georgia, serif; font-size: 10px; color: var(--brand-green); margin-top: 5px; }
  .footer-band {
    position: absolute; left: 0; bottom: 0; width: 100%; height: 43px;
    background: var(--brand-green); text-align: center;
  }
  .footer-url {
    font-family: "Aleo", Georgia, serif; font-size: 10px; letter-spacing: 0.8px;
    color: var(--paper); line-height: 14px; margin-top: 11px;
  }
  .footer-tab {
    position: absolute; left: 223px; bottom: 0; width: 163px; height: 9px;
    background: var(--paper); border-radius: 8px 8px 0 0;
  }
</style>
</head>
<body>
  <div class="letterhead">
    <div class="top-band"></div>

    <div class="brand">
      <span class="brand-dot"></span>
      <div class="brand-name">VELMORAN<br>TRAVEL</div>
    </div>

    <div class="address">Mill Lane House, Arden Road,<br>Ballyvara, Co.Clare, Ireland</div>

    <div class="letter">
      <p class="letter-date">Ballyvara, Co.Clare, Ireland, 31. 01. 2021.</p>
      <p class="letter-topic">Today’s topic</p>
      <div class="letter-body">
        <p>Lorem ipsum dolor sit amet, consectetur adipisicing elit, sed do eiusmod tempor incididunt ut labore et dolore magna aliqua. Ut enim ad minim veniam, quis nostrud exercitation ullamco laboris nisi ut aliquip ex ea commodo consequat.</p>
        <p>Duis aute irure dolor in reprehenderit in voluptate velit esse cillum dolore eu fugiat nulla pariatur. Excepteur sint occaecat cupidatat non proident, sunt in culpa qui officia deserunt mollit anim id est laborum.</p>
        <p>Sed ut perspiciatis unde omnis iste natus error sit voluptatem accusantium doloremque laudantium, totam rem aperiam, eaque ipsa quae ab illo inventore veritatis et quasi architecto beatae vitae dicta sunt explicabo.</p>
        <p>Nemo enim ipsam voluptatem quia voluptas sit aspernatur aut odit aut fugit, sed quia consequuntur magni dolores eos qui ratione voluptatem sequi nesciunt. Neque porro quisquam est, qui dolorem ipsum quia dolor sit amet, consectetur, adipisci velit, sed quia non numquam eius modi tempora incidunt ut labore et dolore magnam aliquam quaerat voluptatem.</p>
        <p>Ut enim ad minima veniam, quis nostrum exercitationem ullam corporis suscipit laboriosam, nisi ut aliquid ex ea commodi consequatur?</p>
        <p>Quis autem vel eum iure reprehenderit qui in ea voluptate velit esse quam nihil molestiae consequatur, vel illum qui dolorem eum fugiat quo voluptas nulla pariatur?</p>
        <p>Duis aute irure dolor in reprehenderit in voluptate velit esse cillum dolore eu fugiat nulla pariatur. Excepteur sint occaecat cupidatat non proident, sunt in culpa qui officia deserunt mollit anim id est laborum.</p>
        <p>Lorem ipsum dolor sit amet, consectetur adipisicing elit, sed do eiusmod tempor incididunt ut labore et dolore magna aliqua. Ut enim ad minim veniam, quis nostrud exercitation ullamco laboris nisi ut aliquip ex ea commodo consequat.</p>
      </div>
    </div>

    <div class="signature" role="img" aria-label="Handwritten signature of the sender"></div>

    <div class="contacts">
      <div class="contact" style="left:120px;">
        <svg width="14" height="14" viewBox="0 0 14 14" aria-hidden="true">
          <circle cx="7" cy="7" r="6.5" fill="#2a3f8f"/>
          <rect x="0.5" y="5.5" width="13" height="3" fill="#fff"/>
          <rect x="5.5" y="0.5" width="3" height="13" fill="#fff"/>
          <rect x="0.5" y="6.2" width="13" height="1.6" fill="#c8202f"/>
          <rect x="6.2" y="0.5" width="1.6" height="13" fill="#c8202f"/>
        </svg>
        <p class="contact-number">0800 041 5527</p>
        <p class="contact-label">UK FreeFone</p>
      </div>
      <div class="contact" style="left:304px;">
        <svg width="26" height="14" viewBox="0 0 26 14" aria-hidden="true">
          <circle cx="7" cy="7" r="6.5" fill="#2a3f8f"/>
          <circle cx="18" cy="7" r="6.5" fill="#d8262f"/>
          <rect x="15" y="2" width="6" height="10" fill="#fff"/>
        </svg>
        <p class="contact-number">1877 604 3318</p>
        <p class="contact-label">USA &amp; Canada</p>
      </div>
      <div class="contact" style="left:489px;">
        <svg width="14" height="14" viewBox="0 0 14 14" aria-hidden="true">
          <circle cx="7" cy="7" r="6" fill="#2f57b8" stroke="#1e3a86" stroke-width="1"/>
          <ellipse cx="7" cy="7" rx="2.6" ry="6" fill="none" stroke="#fff" stroke-width="0.8"/>
          <line x1="1" y1="7" x2="13" y2="7" stroke="#fff" stroke-width="0.8"/>
          <line x1="2" y1="4" x2="12" y2="4" stroke="#fff" stroke-width="0.6"/>
          <line x1="2" y1="10" x2="12" y2="10" stroke="#fff" stroke-width="0.6"/>
        </svg>
        <p class="contact-number">+353 65 48213</p>
        <p class="contact-label">International</p>
      </div>
    </div>

    <div class="footer-band">
      <p class="footer-url">www.VelmoranTravel.com</p>
      <div class="footer-tab"></div>
    </div>
  </div>
</body>
</html>
```